Design of an attractive membership brochure/membership card for an Electrical Business

Hi, we are an electrical business based in Sydney, Australia.

Our design's aim is to attract and target new customers into using our business as a repeat for anything electrical in their home. We would be handing this out to them after a job is completed and they're happy with the service.
We're thinking of a brochure, possibly additional membership cards with personalized number ID's for each client.

Open to ideas, but some of the things we want to include on our brochure are perks of why the client should sign up with us as a lifetime client
- Discounted emergency call out fees outside of normal hours
- Lifetime membership price, one time payment
- Exclusive 10% member discount on all future jobs
- Priority on any during business hour jobs or emergencies

If any other questions please don't hesitate to reach out.
We've attached our logo for reference for the mock designs.
Our website
https://brightwirehaus.com.au/

```html
<!DOCTYPE html>
<html lang="en">
<head>
<meta charset="utf-8">
<title>Brightwire Haus – Membership Brochure</title>
<link href="https://fonts.googleapis.com/css2?family=Audiowide&family=Poppins:wght@400;600;800&display=swap" rel="stylesheet">
<style>
:root{
  --stage:#d3d3d3;
  --ink:#2b2b2b;
  --ink-deep:#161616;
  --ink-soft:#3a3a3a;
  --red:#f04a3a;
  --red-text:#ef3b2d;
  --white:#ffffff;
  --muted:#cfcfcf;
}
*{box-sizing:border-box;margin:0;padding:0}
html,body{width:800px;height:1200px;overflow:hidden;background:var(--stage)}
body{font-family:"Poppins",sans-serif;color:var(--white)}
.canvas{position:relative;width:800px;height:1200px;overflow:hidden;background:var(--stage)}
.spread{position:absolute;left:20px;width:760px;height:520px;display:flex;box-shadow:0 6px 18px rgba(0,0,0,.25)}
.spread--outside{top:40px}
.spread--inside{top:640px}
.panel{position:relative;width:380px;height:520px;overflow:hidden;background:linear-gradient(160deg,var(--ink-soft),var(--ink) 55%,var(--ink-deep))}
.panel__art{position:absolute;inset:0}

/* back panel */
.back{padding:22px 24px}
.back__kicker{font-weight:800;font-size:12px;text-transform:uppercase;letter-spacing:.3px}
.back__title{font-weight:800;font-size:23px;color:var(--red-text);text-transform:uppercase;line-height:1.05}
.rule{height:3px;background:var(--white);margin:10px -24px}
.perks{list-style:none;font-weight:800;font-size:10.5px;text-transform:uppercase;line-height:1.35}
.perks li{margin-bottom:5px}
.section-title{font-family:"Audiowide",sans-serif;color:var(--red-text);font-size:17px;margin-bottom:6px}
.about__text{font-size:9.6px;line-height:1.45;color:var(--muted)}
.contact__list{list-style:none;font-size:10.5px;line-height:1.6}
.contact__list li{display:flex;align-items:center;gap:6px}
.dot{width:8px;height:8px;border-radius:50%;background:var(--red)}
.follow{position:absolute;right:24px;bottom:18px;display:flex;align-items:center;gap:5px;font-size:10px;color:var(--red-text)}
.follow__box{width:10px;height:10px;border:1.5px solid var(--white);border-radius:2px}

/* front panel */
.brand{position:absolute;left:26px;top:40px;display:flex;align-items:center;gap:8px}
.brand__square{width:14px;height:14px;background:var(--red)}
.brand__name{font-weight:800;font-size:17px;color:var(--white);text-transform:uppercase;letter-spacing:1px;line-height:1.1}
.headline{position:absolute;left:26px;bottom:26px;font-family:"Audiowide",sans-serif;font-size:21px;line-height:1.25}
.headline em{font-style:normal;color:var(--red-text)}

/* inside */
.svc{position:absolute;display:flex;gap:7px}
.svc__icon{flex:none;width:20px;height:20px;border-radius:50%;background:var(--white);display:flex;align-items:center;justify-content:center}
.svc__icon span{width:8px;height:8px;border:1.5px solid var(--ink);border-radius:2px}
.svc__title{font-weight:800;font-size:8.5px;color:var(--red-text);text-transform:uppercase;line-height:1.15;border-bottom:1px solid #6a6a6a;padding-bottom:2px;margin-bottom:3px}
.svc__text{font-size:6.8px;line-height:1.4;color:var(--muted)}
.brand--inside{left:auto;right:24px;top:auto;bottom:26px}
.brand--inside .brand__name{font-size:13px}
</style>
</head>
<body>
<main class="canvas">

  <!-- outside spread -->
  <section class="spread spread--outside">
    <article class="panel back">
      <p class="back__kicker">Why the client should sign up with us</p>
      <h2 class="back__title">As a lifetime client</h2>
      <div class="rule"></div>
      <ol class="perks">
        <li>1. Discounted emergency call out fees outside of normal hours</li>
        <li>2. Lifetime membership price, one time payment</li>
        <li>3. Exclusive 10% member discount on all future jobs</li>
        <li>4. Priority on any during business hour jobs or emergencies</li>
      </ol>
      <div class="rule"></div>
      <h3 class="section-title">About Us :</h3>
      <p class="about__text">Brightwire Haus is a Sydney-based electrical business specialising in electrical maintenance work for residential, commercial, strata and real estate clients. It began with two mates with a strong desire to change the image of tradies and provide exceptional service. As a team of electricians based in the Inner West of Sydney, we understand the need of everyday people struggling to find good, reliable and trustworthy electricians. At Brightwire Haus, we have high expectations of ourselves and strive to improve every day.</p>
      <div class="rule"></div>
      <h3 class="section-title">Contact Us :</h3>
      <ul class="contact__list">
        <li><span class="dot"></span>Marcus Hale - 0412555018</li>
        <li><span class="dot"></span>brightwirehaus.com.au</li>
        <li><span class="dot"></span>services@brightwirehaus.com.au</li>
      </ul>
      <div class="follow">Follow Us On : <span class="follow__box"></span><span class="follow__box"></span></div>
    </article>

    <article class="panel front">
      <svg class="panel__art" viewBox="0 0 380 520" aria-hidden="false">
        <polygon points="245,18 380,18 380,330 195,300" fill="#4a4a4a" stroke="#fff" stroke-width="4" role="img" aria-label="Photo of a dark modern interior"/>
        <polygon points="18,250 380,318 380,440 18,372" fill="#d8cfc2" stroke="#fff" stroke-width="4" role="img" aria-label="Photo of a bright modern bathroom with timber vanity"/>
        <polygon points="0,430 380,460 380,520 0,520" fill="#111"/>
      </svg>
      <div class="brand"><span class="brand__square"></span><span class="brand__name">Brightwire<br>Haus</span></div>
      <h1 class="headline">Are You Looking For<br><em>Electricians</em> based in Sydney?</h1>
    </article>
  </section>

  <!-- inside spread -->
  <section class="spread spread--inside">
    <article class="panel">
      <svg class="panel__art" viewBox="0 0 380 520">
        <polygon points="0,0 240,0 0,230" fill="var(--red)"/>
        <rect x="40" y="50" width="120" height="120" transform="rotate(-12 100 110)" fill="#3c4a66" stroke="#111" stroke-width="4" role="img" aria-label="Photo of a modern brick house at dusk"/>
      </svg>
      <div class="svc" style="left:190px;top:34px;width:170px"><div class="svc__icon"><span></span></div><div><p class="svc__title">Surge Protection</p><p class="svc__text">Surges from storms or grid faults can burn out costly appliances. A surge protector keeps your home safe.</p></div></div>
      <div class="svc" style="left:190px;top:130px;width:170px"><div class="svc__icon"><span></span></div><div><p class="svc__title">Switchboard Upgrade and Repairs</p><p class="svc__text">Switchboards are the heart of your home. We repair, relocate or install brand-new boards with the latest protection.</p></div></div>
      <div class="svc" style="left:24px;top:262px;width:336px"><div class="svc__icon"><span></span></div><div><p class="svc__title">Hot Water Diagnosis &amp; Repair</p><p class="svc__text">We do 24/7 hot water repairs. Our vans are always stocked so we diagnose and fix your issue fast.</p></div></div>
      <div class="svc" style="left:24px;top:306px;width:336px"><div class="svc__icon"><span></span></div><div><p class="svc__title">TV Antenna Installation &amp; Diagnostics</p><p class="svc__text">We install TV aerials, connection points and wall mounts, with cabling neatly concealed but easy to reach.</p></div></div>
      <div class="svc" style="left:24px;top:350px;width:336px"><div class="svc__icon"><span></span></div><div><p class="svc__title">Data &amp; NBN</p><p class="svc__text">We install data points and WiFi access points throughout your home for the best speed.</p></div></div>
      <div class="svc" style="left:24px;top:394px;width:336px"><div class="svc__icon"><span></span></div><div><p class="svc__title">Renovation and Fitouts</p><p class="svc__text">Renovating your kitchen, bathroom or whole house? We handle all power, lighting and data cabling.</p></div></div>
      <div class="svc" style="left:24px;top:438px;width:230px"><div class="svc__icon"><span></span></div><div><p class="svc__title">Appliance Installation</p><p class="svc__text">We install your new oven, cooktop or rangehood with care, as if they were our own.</p></div></div>
      <div class="brand brand--inside"><span class="brand__square"></span><span class="brand__name">Brightwire Haus</span></div>
    </article>

    <article class="panel">
      <svg class="panel__art" viewBox="0 0 380 520">
        <polygon points="140,0 380,0 380,220" fill="var(--red)"/>
        <rect x="230" y="30" width="120" height="120" transform="rotate(-12 290 90)" fill="#4f6b2e" stroke="#111" stroke-width="4" role="img" aria-label="Photo of a garden path light among green shrubs"/>
      </svg>
      <div class="svc" style="left:20px;top:30px;width:200px"><div class="svc__icon"><span></span></div><div><p class="svc__title">Lighting Layout Design and Installations</p><p class="svc__text">We plan and install indoor and garden lighting that suits every room and outdoor space.</p></div></div>
      <div class="svc" style="left:20px;top:112px;width:200px"><div class="svc__icon"><span></span></div><div><p class="svc__title">Emergency Services</p><p class="svc__text">Our team is available 24 hours for urgent electrical work, fully stocked to fix it fast.</p></div></div>
      <div class="svc" style="left:20px;top:196px;width:340px"><div class="svc__icon"><span></span></div><div><p class="svc__title">Smoke Alarm Installations and Testing</p><p class="svc__text">We install and test smoke alarms so you know your home or rental is safe.</p></div></div>
      <div class="svc" style="left:20px;top:244px;width:340px"><div class="svc__icon"><span></span></div><div><p class="svc__title">Level 2 Electrician</p><p class="svc__text">Accredited for network connections, overhead and underground mains and metering.</p></div></div>
      <div class="svc" style="left:20px;top:292px;width:340px"><div class="svc__icon"><span></span></div><div><p class="svc__title">Ceiling Fans, Exhaust Fans &amp; General Ventilation</p><p class="svc__text">Beat the summer heat and keep rooms mold-free. We supply, install and warranty every fan.</p></div></div>
      <div class="svc" style="left:20px;top:346px;width:340px"><div class="svc__icon"><span></span></div><div><p class="svc__title">Powerpoint Installations or Repair</p><p class="svc__text">Tired of messy power leads? We add new power points anywhere and replace damaged ones.</p></div></div>
      <div class="svc" style="left:20px;top:400px;width:340px"><div class="svc__icon"><span></span></div><div><p class="svc__title">Electrical Fault Finding</p><p class="svc__text">Faults can cause loss of power or damage. We track down the cause and provide a lasting solution.</p></div></div>
    </article>
  </section>

</main>
</body>
</html>
```